Design for Cedar Lark Homes real estate agency

Incorporate logo into new business cards. I need to include the Brindley Vance logo incorporated into Cedar Lark Homes on one side of the card (attached). On the other side I see just the icon with "Maren Quill" (attached) with "Grounded in Integrity" either included as is or removed from logo and rather put as a tag line on the business card separate from the main logo. Contact information:

Maren Quill
Associate Broker
Cell: 730-418-5093
Email: marenquill@cedarlarkhomes.example
Web: www.cedarlarkhomes.example

Target Market(s)

Buyers, Sellers, Builders and Investors of homes and land

Industry/Entity Type

Real Estate Agent

Contact Information for Business Card

My client base tend to be higher end home buyers, sellers, builders and investors. I have been more and more in land and subdivisions for builders and investors. The card should not be cluttered. Clean and simple - yet with an air of exclusive/high end

Colors

Designer to choose colors to be used in the design.

Requirements
Must have
• Must have the logo on one side that has Brindley Vance logo incorporated. The side that has my contact information does not have to have the Brindley Vance logo incorporated.
• Must include "Grounded in Integrity" tag line either within logo (as is) or removed from logo and included in another position on the side of the business card with contact information.
Should not have
• Should not have Brindley Vance logo incorporated into Cedar Lark Homes logo on both sides of business card. Would like the Cedar Lark Homes logo that has Brindley Logo only on the back side of card without contact information.

```html
<!DOCTYPE html>
<html lang="en">
<head>
<meta charset="utf-8">
<title>Cedar Lark Homes – Business Cards</title>
<link href="https://fonts.googleapis.com/css2?family=Cinzel:wght@400;600&family=Playfair+Display:wght@600&family=Open+Sans:wght@400;600&display=swap" rel="stylesheet">
<style>
  :root {
    --bg: #d9d6d0;
    --card: #ffffff;
    --brown: #6b4a0c;
    --brown-dark: #4a3208;
    --gold: #c9a21c;
    --gold-light: #e3c55a;
    --ink: #5a3f10;
    --grey: #6d6d6d;
    --white: #ffffff;
  }
  * { box-sizing: border-box; margin: 0; padding: 0; }
  html, body { width: 1200px; height: 900px; overflow: hidden; background: var(--bg); }
  .canvas { position: relative; width: 1200px; height: 900px; }
  .card {
    position: absolute; width: 620px; height: 354px;
    background: var(--card); overflow: hidden;
    box-shadow: 0 6px 18px rgba(0,0,0,.18);
  }
  .card--front { left: 290px; top: 70px; }
  .card--back { left: 290px; top: 476px; }

  /* Front */
  .brand { position: absolute; left: 118px; top: 108px; display: flex; align-items: center; gap: 16px; }
  .brand__mark { width: 62px; height: 62px; border-radius: 50%; background: var(--gold); flex: none; }
  .brand__text { display: flex; flex-direction: column; align-items: center; }
  .brand__name { font-family: "Playfair Display", serif; font-weight: 600; font-size: 34px; color: var(--ink); line-height: 1; white-space: nowrap; }
  .brand__rule { width: 100%; height: 1px; background: var(--ink); margin: 6px 0 4px; }
  .brand__agent { font-family: "Cinzel", serif; font-size: 13px; letter-spacing: 3px; color: var(--ink); white-space: nowrap; }
  .brand__tag { font-family: "Cinzel", serif; font-size: 8px; letter-spacing: 2.5px; color: var(--grey); margin-top: 2px; white-space: nowrap; }
  .partner-badge { width: 30px; height: 30px; background: var(--brown-dark); align-self: flex-start; margin-top: 2px; flex: none; }
  .front-web { position: absolute; left: 0; right: 0; top: 270px; text-align: center;
    font-family: "Open Sans", sans-serif; font-size: 13px; letter-spacing: 4px; color: var(--grey); }

  /* Back */
  .back-shape { position: absolute; inset: 0; }
  .contact { position: absolute; left: 34px; top: 206px; color: var(--white); font-family: "Open Sans", sans-serif; }
  .contact__name { font-weight: 600; font-size: 16px; color: var(--gold-light); text-transform: uppercase; }
  .contact__role { font-size: 15px; text-transform: uppercase; margin-bottom: 10px; }
  .contact__line { display: flex; align-items: center; gap: 9px; font-size: 14px; line-height: 22px; white-space: nowrap; }
  .contact__icon { width: 12px; height: 12px; flex: none; }
  .identity { position: absolute; left: 340px; top: 64px; width: 260px; display: flex; flex-direction: column; align-items: center; }
  .identity__mark { width: 84px; height: 84px; border-radius: 50%; background: var(--gold); }
  .identity__name { font-family: "Cinzel", serif; font-weight: 600; font-size: 26px; letter-spacing: 3px; color: var(--ink); margin-top: 18px; white-space: nowrap; }
  .identity__tag { font-family: "Cinzel", serif; font-size: 9px; letter-spacing: 3px; color: var(--grey); margin-top: 2px; white-space: nowrap; }
</style>
</head>
<body>
<main class="canvas">
  <section class="card card--front">
    <div class="brand">
      <div class="brand__mark"></div>
      <div class="brand__text">
        <span class="brand__name">Cedar Lark Homes</span>
        <span class="brand__rule"></span>
        <span class="brand__agent">MAREN QUILL</span>
        <span class="brand__tag">GROUNDED IN INTEGRITY</span>
      </div>
      <div class="partner-badge"></div>
    </div>
    <p class="front-web">www.cedarlarkhomes.example</p>
  </section>

  <section class="card card--back">
    <svg class="back-shape" viewBox="0 0 620 354" width="620" height="354">
      <path d="M0,0 L232,0 C312,50 338,130 316,196 C296,262 392,330 500,354 L0,354 Z" fill="var(--gold)"/>
      <path d="M0,0 L214,0 C296,54 322,130 298,196 C276,262 370,330 470,354 L0,354 Z" fill="var(--white)"/>
      <path d="M0,0 L204,0 C284,56 310,130 286,196 C264,262 356,330 452,354 L0,354 Z" fill="var(--brown)"/>
    </svg>
    <div class="contact">
      <p class="contact__name">Maren Quill</p>
      <p class="contact__role">Associate Broker</p>
      <p class="contact__line">
        <svg class="contact__icon" viewBox="0 0 12 12"><rect x="3" y="0.5" width="6" height="11" rx="1.2" fill="none" stroke="var(--gold-light)" stroke-width="1.2"/></svg>
        730-418-5093
      </p>
      <p class="contact__line">
        <svg class="contact__icon" viewBox="0 0 12 12"><rect x="0.5" y="2" width="11" height="8" fill="var(--gold-light)"/><path d="M0.5,2 L6,6.5 L11.5,2" fill="none" stroke="var(--brown)" stroke-width="1"/></svg>
        marenquill@cedarlarkhomes.example
      </p>
      <p class="contact__line">
        <svg class="contact__icon" viewBox="0 0 12 12"><circle cx="6" cy="6" r="5.5" fill="var(--gold-light)"/><path d="M0.5,6 H11.5 M6,0.5 C3,4 3,8 6,11.5 M6,0.5 C9,4 9,8 6,11.5" fill="none" stroke="var(--brown)" stroke-width="0.8"/></svg>
        www.cedarlarkhomes.example
      </p>
    </div>
    <div class="identity">
      <div class="identity__mark"></div>
      <span class="identity__name">MAREN QUILL</span>
      <span class="identity__tag">GROUNDED IN INTEGRITY</span>
    </div>
  </section>
</main>
</body>
</html>
```